Greeting Card Design Project

We need a greeting card to email our clients during christmas.

We are suppliers for cutting tools & machine accessories. You can find out more about us at our website www.tovrana.com.sg

Reason: I've decide to extend the deadline as I'm awaiting more designs, thank you.

```html
<!DOCTYPE html>
<html lang="en">
<head>
<meta charset="utf-8">
<title>Happy Holidays – Tovrana Tools</title>
<link rel="stylesheet" href="https://fonts.googleapis.com/css2?family=Pathway+Gothic+One:ital@0;1&display=swap">
<style>
  :root {
    --frost: #cedbdb;
    --snow: #ffffff;
    --holly-red: #e8232f;
    --pine-green: #1e9a4b;
  }
  html, body {
    margin: 0;
    padding: 0;
    overflow: hidden;
    background: var(--frost);
  }
  .card {
    position: relative;
    width: 928px;
    height: 1200px;
    overflow: hidden;
    background: var(--frost);
    font-family: "Pathway Gothic One", "Arial Narrow", sans-serif;
  }
  .card__frost {
    position: absolute;
    inset: 0;
  }
  .card__greeting {
    position: absolute;
    top: 122px;
    left: 0;
    width: 100%;
    margin: 0;
    text-align: center;
    font-size: 124px;
    line-height: 1;
    font-weight: 400;
    letter-spacing: 5px;
    color: var(--holly-red);
  }
  .card__brand-mark {
    position: absolute;
    top: 255px;
    left: 369px;
    width: 190px;
    height: 190px;
    border-radius: 50%;
    background: var(--pine-green);
  }
  .card__brand {
    position: absolute;
    top: 466px;
    left: 0;
    width: 100%;
    margin: 0;
    text-align: center;
    font-size: 124px;
    line-height: 1;
    font-weight: 400;
    letter-spacing: 4px;
    color: var(--holly-red);
  }
  .card__message {
    position: absolute;
    top: 682px;
    left: 0;
    width: 100%;
    margin: 0;
    text-align: center;
    font-size: 58px;
    line-height: 60px;
    letter-spacing: 3px;
    color: var(--pine-green);
  }
  .card__message em {
    font-style: italic;
  }
</style>
</head>
<body>
<main class="card">
  <svg class="card__frost" width="928" height="1200" viewBox="0 0 928 1200" aria-hidden="true">
    <defs>
      <pattern id="teeth-top" x="0" y="0" width="38" height="56" patternUnits="userSpaceOnUse">
        <path d="M0 0 H38 V18 L30 22 L24 54 L18 24 L9 40 L4 20 L0 22 Z" fill="var(--snow)"/>
      </pattern>
      <pattern id="teeth-bottom" x="0" y="1144" width="38" height="56" patternUnits="userSpaceOnUse">
        <path d="M0 56 H38 V38 L31 34 L26 4 L19 32 L11 16 L6 36 L0 34 Z" fill="var(--snow)"/>
      </pattern>
      <pattern id="teeth-left" x="0" y="0" width="56" height="38" patternUnits="userSpaceOnUse">
        <path d="M0 0 V38 H18 L22 31 L54 26 L24 19 L40 11 L20 6 L22 0 Z" fill="var(--snow)"/>
      </pattern>
      <pattern id="teeth-right" x="872" y="0" width="56" height="38" patternUnits="userSpaceOnUse">
        <path d="M56 0 V38 H38 L34 31 L2 26 L32 19 L16 11 L36 6 L34 0 Z" fill="var(--snow)"/>
      </pattern>
    </defs>
    <rect x="0" y="0" width="928" height="1200" fill="var(--frost)"/>
    <rect x="0" y="0" width="928" height="56" fill="url(#teeth-top)"/>
    <rect x="0" y="1144" width="928" height="56" fill="url(#teeth-bottom)"/>
    <rect x="0" y="0" width="56" height="1200" fill="url(#teeth-left)"/>
    <rect x="872" y="0" width="56" height="1200" fill="url(#teeth-right)"/>
  </svg>

  <h1 class="card__greeting">HAPPY HOLIDAYS</h1>

  <div class="card__brand-mark" aria-hidden="true"></div>
  <p class="card__brand">TOVRANA TOOLS</p>

  <p class="card__message">
    THE BITTERNESS OF POOR QUALITY<br>
    REMAINS LONG AFTER THE<br>
    SWEETNESS OF THE<br>
    <em>HOLIDAY SEASON</em> IS FORGOTTEN
  </p>
</main>
</body>
</html>
```